Business Card Design using new logo

As much as we'd like to think that treating everyone equally is the best strategy for fairness, the reality is that the differences in the lives of women and men have to be taken into account to ensure that organizations, programs, services, and yes, even public policy treat women and men in ways that achieve gender equity.

That's where ParityLumen - fairness metrics insight comes in. Using the data-driven tools of gender analysis, our organization can help anyone determine if gender equity is being achieved - in businesses and organizations, in the planning and implementation of programs and services, and in the development and enforcement of public policy.
Updates

Apologies for the delay - have not had time to finalize the decision.  Should be early this week - probably Tuesday.

Industry/Entity Type

Business

Requirements
Must have
• New Logo for ParityLumen
• Logo plus words "Fairness Metrics Insight"

```html
<!DOCTYPE html>
<html lang="en">
<head>
<meta charset="utf-8">
<title>ParityLumen Business Card</title>
<link rel="stylesheet" href="https://fonts.googleapis.com/css2?family=Open+Sans:wght@400;600;700&display=swap">
<style>
  :root {
    --backdrop: #cfcfcf;
    --charcoal: #414141;
    --charcoal-deep: #383838;
    --paper: #f5f5f5;
    --amber: #e8952a;
    --ash: #9a9a9a;
    --ink-light: #f2f2f2;
  }
  * { margin: 0; padding: 0; box-sizing: border-box; }
  html, body {
    width: 1200px;
    height: 900px;
    overflow: hidden;
    background: var(--backdrop);
    font-family: "Open Sans", Arial, sans-serif;
  }
  .card {
    position: absolute;
    left: 300px;
    width: 600px;
    height: 343px;
    overflow: hidden;
    box-shadow: 0 2px 6px rgba(0,0,0,0.15);
  }
  /* Front face */
  .card-front {
    top: 80px;
    background: var(--charcoal);
    display: flex;
    align-items: center;
    justify-content: center;
  }
  .front-lockup {
    display: flex;
    align-items: center;
    gap: 16px;
  }
  .brand-dot {
    width: 54px;
    height: 54px;
    border-radius: 50%;
    background: var(--amber);
    flex: none;
  }
  .front-words { display: flex; flex-direction: column; }
  .front-name {
    color: var(--ink-light);
    font-size: 42px;
    font-weight: 600;
    line-height: 1.05;
    letter-spacing: -0.5px;
  }
  .front-tagline {
    color: var(--amber);
    font-size: 19px;
    font-weight: 400;
    margin-top: 4px;
    letter-spacing: 0.3px;
  }
  /* Back face */
  .card-back {
    top: 477px;
    background: var(--charcoal);
  }
  .back-header {
    height: 98px;
    background: var(--paper);
    border-bottom: 5px solid var(--amber);
    display: flex;
    align-items: center;
    justify-content: space-between;
    padding: 0 34px 0 28px;
  }
  .back-lockup { display: flex; align-items: center; gap: 10px; }
  .back-lockup .brand-dot { width: 34px; height: 34px; }
  .back-name {
    color: var(--charcoal);
    font-size: 30px;
    font-weight: 600;
    letter-spacing: -0.3px;
  }
  .web-address {
    color: var(--charcoal);
    font-size: 15px;
    letter-spacing: 1px;
  }
  .back-body {
    display: flex;
    align-items: center;
    height: 240px;
  }
  .holder-name {
    width: 290px;
    padding-left: 52px;
    color: var(--ink-light);
    font-size: 20px;
    font-weight: 700;
  }
  .divider {
    width: 2px;
    height: 112px;
    background: var(--ash);
    margin-right: 22px;
  }
  .contact-list { list-style: none; }
  .contact-item {
    display: flex;
    align-items: center;
    gap: 14px;
    color: var(--ink-light);
    font-size: 14px;
    letter-spacing: 0.6px;
    line-height: 26px;
  }
  .contact-icon { width: 14px; height: 14px; flex: none; fill: var(--amber); }
</style>
</head>
<body>
  <section class="card card-front" aria-label="Business card front">
    <div class="front-lockup">
      <span class="brand-dot"></span>
      <div class="front-words">
        <span class="front-name">ParityLumen</span>
        <span class="front-tagline">Fairness Metrics Insight</span>
      </div>
    </div>
  </section>

  <section class="card card-back" aria-label="Business card back">
    <header class="back-header">
      <div class="back-lockup">
        <span class="brand-dot"></span>
        <span class="back-name">ParityLumen</span>
      </div>
      <span class="web-address">www.paritylumen.com</span>
    </header>
    <div class="back-body">
      <div class="holder-name">Martin Kealy</div>
      <div class="divider"></div>
      <ul class="contact-list">
        <li class="contact-item">
          <svg class="contact-icon" viewBox="0 0 16 16" aria-hidden="true"><path d="M3.5 1.5l2.5 0 1 3.5-1.8 1.3c.9 1.9 2.4 3.4 4.3 4.3L10.8 9l3.5 1v2.5c0 1-1 2-2 2C6.8 14.5 1.5 9.2 1.5 3.5c0-1 1-2 2-2z"/></svg>
          353 555 0140
        </li>
        <li class="contact-item">
          <svg class="contact-icon" viewBox="0 0 16 16" aria-hidden="true"><path d="M4.5 1h7c.6 0 1 .4 1 1v12c0 .6-.4 1-1 1h-7c-.6 0-1-.4-1-1V2c0-.6.4-1 1-1zm.8 2v8.5h5.4V3zM8 12.3a.9.9 0 100 1.8.9.9 0 000-1.8z"/></svg>
          353 555 0141
        </li>
        <li class="contact-item">
          <svg class="contact-icon" viewBox="0 0 16 16" aria-hidden="true"><path d="M1 3.5h14v1L8 9 1 4.5zM1 6l7 4.5L15 6v6.5H1z"/></svg>
          info@paritylumen.com
        </li>
        <li class="contact-item">
          <svg class="contact-icon" viewBox="0 0 16 16" aria-hidden="true"><circle cx="8" cy="8" r="6"/></svg>
          @Parity_Lumen
        </li>
      </ul>
    </div>
  </section>
</body>
</html>
```